Emergency Medical Training and Events Company Business Needs Business Card Design

We are in need of a business card for our dynamic company expanding its customer base and need to be easily contacted and identified for when we visit with government officials, potential EMS / Fire agencies and county coordinators to arrange for training programs for first responders to better prepare them for critical thinking at critical incidents.
Updates

Need extra days to review

Target Market(s)

EMS/Fire and Event Promoters

Industry/Entity Type

Medical

Contact Information for Business Card

Two cards, comparable designs:

Gavin R. Thorley, Principal, g.thorley@vantrexmed.com
Neil Carrow, Event and Training Specialist, n.carrow@vantrexmed.com

Font styles to use
Other font styles liked:
• Cambria

Colors

Designer to choose colors to be used in the design.

Requirements
Must have
• Company Logo, Spots for Name, Title, Phone Number, Email, Website
• A bullet list stating that we offer, KMB CPR and First Aid Instructors, Hold the Line Instructors, Event EMS, CME's, MCI Training and Planning. We prefer to have a black background for the card but if you can make a blue or white card stand out we would review that as well.
Should not have
• Tacky logos or special sayings ... simple, elegant, professional is the look we seek

```html
<!DOCTYPE html>
<html lang="en">
<head>
<meta charset="utf-8">
<title>Vantrex Medical – Business Card</title>
<link rel="stylesheet" href="https://fonts.googleapis.com/css2?family=Montserrat:wght@400;500;600;700&display=swap">
<style>
  :root {
    --navy: #1c1f5c;
    --red: #d0202a;
    --white: #ffffff;
    --ink: #3a3a44;
    --rule: #d9d9de;
    --backdrop: #2a2b2f;
  }
  * { box-sizing: border-box; margin: 0; padding: 0; }
  html, body { width: 1200px; height: 900px; overflow: hidden; }
  body {
    background: var(--backdrop);
    font-family: "Montserrat", Arial, sans-serif;
    display: flex;
    flex-direction: column;
    align-items: center;
    justify-content: center;
    gap: 50px;
  }
  .card {
    width: 560px;
    height: 320px;
    position: relative;
    overflow: hidden;
    box-shadow: 0 10px 30px rgba(0,0,0,.35);
  }

  /* Front */
  .card-front { background: var(--white); display: flex; align-items: center; }
  .brand {
    width: 260px;
    display: flex;
    align-items: center;
    justify-content: center;
    gap: 12px;
  }
  .brand-dot { width: 34px; height: 34px; border-radius: 50%; background: var(--navy); flex: none; }
  .brand-name {
    color: var(--navy);
    font-weight: 700;
    font-size: 24px;
    line-height: 1.05;
    letter-spacing: .5px;
  }
  .divider { width: 1px; height: 200px; background: var(--rule); }
  .contact { padding-left: 34px; }
  .person-name { color: var(--navy); font-weight: 700; font-size: 20px; letter-spacing: .5px; }
  .person-title { color: var(--ink); font-size: 13px; margin: 2px 0 18px; }
  .contact-list { list-style: none; }
  .contact-list li {
    display: flex; align-items: center; gap: 10px;
    color: var(--ink); font-size: 14.5px; line-height: 1.65;
  }
  .contact-list svg { width: 14px; height: 14px; fill: var(--navy); flex: none; }

  /* Back */
  .card-back { background: var(--navy); }
  .back-brand {
    position: absolute; left: 0; right: 0; top: 0; height: 236px;
    display: flex; align-items: center; justify-content: center; gap: 16px;
  }
  .back-brand .brand-dot { width: 46px; height: 46px; background: var(--white); }
  .back-brand .brand-name { color: var(--white); font-size: 32px; }
  .services {
    position: absolute; left: 0; right: 0; bottom: 0; height: 84px;
    background: var(--red);
    color: var(--white);
    font-size: 14px; font-weight: 500;
    display: flex; flex-direction: column; justify-content: center;
    padding-left: 30px; line-height: 1.5;
  }
</style>
</head>
<body>

  <section class="card card-front" aria-label="Business card front">
    <div class="brand">
      <span class="brand-dot"></span>
      <span class="brand-name">VANTREX<br>MEDICAL</span>
    </div>
    <div class="divider"></div>
    <div class="contact">
      <p class="person-name">NEIL CARROW</p>
      <p class="person-title">Partner</p>
      <ul class="contact-list">
        <li>
          <svg viewBox="0 0 24 24"><path d="M6.6 10.8a15 15 0 0 0 6.6 6.6l2.2-2.2c.3-.3.7-.4 1-.2 1.1.4 2.3.6 3.6.6.6 0 1 .4 1 1V20c0 .6-.4 1-1 1A17 17 0 0 1 3 4c0-.6.4-1 1-1h3.5c.6 0 1 .4 1 1 0 1.3.2 2.5.6 3.6.1.3 0 .7-.2 1z"/></svg>
          555 014 7890
        </li>
        <li>
          <svg viewBox="0 0 24 24"><path d="M7 1h10a2 2 0 0 1 2 2v18a2 2 0 0 1-2 2H7a2 2 0 0 1-2-2V3a2 2 0 0 1 2-2zm0 3v14h10V4zm5 15.5a1 1 0 1 0 0 2 1 1 0 0 0 0-2z"/></svg>
          555 014 2276
        </li>
        <li>
          <svg viewBox="0 0 24 24"><path d="M2 5h20v14H2zm2 2v.5l8 5 8-5V7l-8 5z"/></svg>
          n.carrow@vantrexmed.com
        </li>
        <li>
          <svg viewBox="0 0 24 24"><path d="M12 2a10 10 0 1 0 0 20 10 10 0 0 0 0-20zm0 2c.9 0 2.2 2 2.7 5H9.3c.5-3 1.8-5 2.7-5zm-7.7 7h3a22 22 0 0 0 0 2h-3a8 8 0 0 1 0-2zm5 0h5.4a20 20 0 0 1 0 2H9.3a20 20 0 0 1 0-2zm7.4 0h3a8 8 0 0 1 0 2h-3a22 22 0 0 0 0-2zM9.3 15h5.4c-.5 3-1.8 5-2.7 5s-2.2-2-2.7-5z"/></svg>
          www.vantrexmed.com
        </li>
      </ul>
    </div>
  </section>

  <section class="card card-back" aria-label="Business card back">
    <div class="back-brand">
      <span class="brand-dot"></span>
      <span class="brand-name">VANTREX<br>MEDICAL</span>
    </div>
    <div class="services">
      <p>KMB CPR and First Aid Instructors • Hold the Line Instructors</p>
      <p>Event EMS • CME's • MCI Training and Planning</p>
    </div>
  </section>

</body>
</html>
```